Tumblewick Youth Sports Academy

I need a family friendly website for children's sports coaching, diets and the importance of children's nutrition, child minding services,children's councilling and physiology services.
Also once I have an understanding of numbers and my fees I will offer a pick up service for my classes

Please add my new logo which is my buisness name,

Target Market(s)

Children of all ages and parents who would like there kids involved in sporting programmes ,

Industry/Entity Type

Nutrition

Requirements
Must have
• Active kids are healthy kids..
Also the logo I have uploaded .
Video call and video calls available for parents to see child's progress and safety at classes if parents are unable to attend.
Nice to have
• Listed about the services I will be offering,
One on one and group sessions.child minding and nanny services, parent and child councilling and physcology services,diet and nutrition personalisation services,pick up services,school visits and motivational classes,
Fully covered and insured business,

```html
<!DOCTYPE html>
<html lang="en">
<head>
<meta charset="utf-8">
<title>Tumblewick Youth Sports Academy</title>
<link rel="stylesheet" href="https://fonts.googleapis.com/css2?family=Open+Sans:wght@400;600;700&display=swap">
<style>
:root{
  --sky-top:#3f9fdf;
  --sky-bottom:#d6eaf5;
  --page:#ffffff;
  --green:#4a9e2f;
  --green-dark:#3b8524;
  --red:#d63a26;
  --blue:#2a74b8;
  --text:#555b60;
  --muted:#8a9096;
  --panel:#eeeff0;
  --rule:#dcdfe2;
  --dark:#3a3f44;
}
*{box-sizing:border-box;margin:0;padding:0}
html,body{width:843px;height:1200px;overflow:hidden}
body{
  font-family:"Open Sans",Arial,sans-serif;
  background:linear-gradient(180deg,var(--sky-top) 0,#7cc0ea 260px,var(--sky-bottom) 700px,#e8f1f6 1200px);
  position:relative;color:var(--text);
}
.page{position:absolute;left:62px;top:0;width:716px;height:1200px;background:var(--page);box-shadow:0 0 12px rgba(0,0,0,.15)}
.brand{position:absolute;left:16px;top:14px;display:flex;align-items:center;gap:10px}
.brand-dot{width:62px;height:62px;border-radius:50%;background:var(--green)}
.brand-name{font-size:15px;font-weight:700;color:var(--green);line-height:1.2;width:150px}
.utility{position:absolute;right:18px;top:38px;display:flex;align-items:center;gap:10px;font-size:10px;font-weight:700;color:var(--blue)}
.utility .sep{color:var(--muted);font-weight:400}
.utility .login{color:var(--red)}
.search{width:130px;height:22px;border:1px solid var(--rule);font-size:10px;color:var(--muted);padding:4px 8px;display:flex;justify-content:space-between;align-items:center;margin-left:8px}
.nav{position:absolute;right:18px;top:88px;display:flex;gap:4px;font-size:11px;color:var(--blue)}
.nav a{padding:4px 9px;text-decoration:none;color:inherit}
.nav a.active{background:var(--green);color:#fff;border-radius:2px}
.hero{position:absolute;left:14px;top:122px;width:688px;height:292px;background:linear-gradient(135deg,#e9d25a 0,#b8cf4e 35%,#6fa93a 70%,#3f8a2e 100%)}
.hero-box{position:absolute;right:22px;top:18px;width:206px;height:254px;background:#fff;padding:18px 14px;text-align:center}
.hero-box h2{font-size:13.5px;font-weight:700;color:var(--red);line-height:1.35}
.hero-box p{font-size:9px;line-height:1.5;margin-top:14px;color:var(--text)}
.dots{display:flex;justify-content:center;gap:7px;margin-top:22px}
.dots span{width:8px;height:8px;border-radius:50%;background:#c4c7ca}
.dots span.on{background:var(--dark)}
.welcome{position:absolute;left:18px;top:436px;width:440px}
h1,h3{font-size:17px;font-weight:700;color:var(--green)}
.welcome p{font-size:9.5px;line-height:1.6;margin-top:10px}
.btn{display:inline-block;margin-top:12px;background:var(--dark);color:#fff;font-size:9.5px;padding:5px 10px;border-radius:2px}
.news{position:absolute;left:478px;top:436px;width:220px}
.news-card{background:var(--panel);margin-top:10px;padding:10px 12px;font-size:9px;line-height:1.5}
.news-card strong{display:block;color:var(--dark);font-weight:600}
.news-card .date{color:var(--red);margin-top:8px}
.services{position:absolute;left:0;top:590px;width:716px;text-align:center}
.services h3{color:var(--red);font-size:18px}
.services .intro{font-size:9px;line-height:1.55;margin:10px auto 0;width:640px}
.grid{display:flex;flex-wrap:wrap;justify-content:center;gap:16px 24px;width:690px;margin:20px auto 0}
.tile{width:150px}
.tile .thumb{height:96px}
.tile span{display:block;font-size:10px;color:var(--blue);margin-top:4px}
.footer{position:absolute;left:18px;right:18px;top:1108px;border-top:1px solid var(--rule);padding-top:10px;font-size:9.5px}
.footer .links{display:flex;gap:10px;color:var(--dark)}
.footer .links i{font-style:normal;color:var(--muted)}
.footer .copy{margin-top:8px;color:var(--muted)}
.social{display:flex;gap:8px;margin-top:10px}
.social span{width:18px;height:18px;border-radius:50%;background:var(--blue)}
.social span.g{background:var(--green)}
.social span.o{background:#e08a2a}
.badge{position:absolute;right:6px;top:10px;width:62px;height:62px;border-radius:50%;background:#c9ced3}
</style>
</head>
<body>
<div class="page">
  <header>
    <div class="brand"><div class="brand-dot"></div><div class="brand-name">Tumblewick Youth Sports Academy</div></div>
    <div class="utility">
      <svg width="16" height="16" viewBox="0 0 16 16" aria-hidden="true"><rect width="16" height="16" rx="3" fill="#2a74b8"/><path d="M5 3.5l2 2-1 1.3c.6 1.3 1.6 2.3 2.9 2.9l1.3-1 2 2-1.2 1.8C7.5 12.2 3.8 8.5 3.5 4.7z" fill="#fff"/></svg>
      <span>CALL US ON VIDEO</span><span class="sep">/</span><span>REGISTER</span><span class="sep">/</span><span class="login">LOGIN</span>
      <div class="search"><span>Search</span>
        <svg width="10" height="10" viewBox="0 0 10 10" aria-hidden="true"><circle cx="4" cy="4" r="3" fill="none" stroke="#8a9096" stroke-width="1.3"/><path d="M6.3 6.3L9 9" stroke="#8a9096" stroke-width="1.3"/></svg></div>
    </div>
    <nav class="nav"><a class="active">Home</a><a>About us</a><a>Services</a><a>Classes</a><a>News</a><a>Testimonials</a><a>Contact us</a></nav>
  </header>

  <section class="hero" role="img" aria-label="Photo of happy children jumping outdoors on a sunny day">
    <div class="hero-box">
      <h2>Donec magna leo, dignis sim diam sollicitudin, auctor consectetur enim.</h2>
      <p>Praesent fermentum diam in metus sagittis. Phasellus auctor nibh sodales lacus tempor, aliquam vestibulum nunc interdum. Fusce et ultricies orci.</p>
      <div class="dots"><span class="on"></span><span></span><span></span><span></span></div>
    </div>
  </section>

  <section class="welcome">
    <h1>Welcome to Tumblewick Youth Sports Academy</h1>
    <p>Aliquam eu lorem vitae nibh mattis dapibus in at arcu. Nullam ornare metus sit amet enim ullamcorper pharetra. Fusce aliquam, arcu ut accumsan tincidunt, odio nisi cursus tellus, at commodo mi mauris sed dolor. In vel diam, gravida vel porttitor quis, condimentum quis ipsum. Curabitur porttitor mi potior tempus lacinia aenean. Quisque lobortis viverra volutpat. Sed at enim lacinia massa tincidunt euismod. Phasellus dictum sem odio, in accumsan urna feugiat leo.</p>
    <span class="btn">Know more</span>
  </section>

  <aside class="news">
    <h3>Latest News</h3>
    <div class="news-card">
      <strong>Suspendisse quis imperdiet</strong>
      Donec magna, dignissim diam sollicitudin, auctor consectetur enim. Praesent fermentum diam in metus.
      <div class="date">January 6, 2014</div>
    </div>
  </aside>

  <section class="services">
    <h3>Our Services</h3>
    <p class="intro">Phasellus blandit scelerisque purus eu dictum. Quisque quis sem luctus, tincidunt urna eget, rutrum mauris. In hac habitasse platea dictumst. Mauris lacinia magna et elementum volutpat. Cum sociis natoque penatibus et magnis dis parturient montes, nascetur ridiculus mus.</p>
    <div class="grid">
      <div class="tile"><div class="thumb" role="img" aria-label="Coach with children in a group session" style="background:linear-gradient(135deg,#6fb0d8,#3f7fae)"></div><span>One on one &amp; Group sessions</span></div>
      <div class="tile"><div class="thumb" role="img" aria-label="Children playing together while minded" style="background:linear-gradient(135deg,#e7b98a,#b5824f)"></div><span>Child Minding</span></div>
      <div class="tile"><div class="thumb" role="img" aria-label="Nanny reading with a child" style="background:linear-gradient(135deg,#d9a06a,#8e5a34)"></div><span>Nanny Services</span></div>
      <div class="tile"><div class="thumb" role="img" aria-label="Parent and child talking with a counsellor" style="background:linear-gradient(135deg,#e8d4c0,#a98c74)"></div><span>Parent &amp; Child Councilling</span></div>
      <div class="tile"><div class="thumb" role="img" aria-label="Child in a psychology session" style="background:linear-gradient(135deg,#e2b590,#b86c4a)"></div><span>Physcology Services</span></div>
      <div class="tile"><div class="thumb" role="img" aria-label="Healthy fruit and vegetables for children" style="background:linear-gradient(135deg,#f0c24a,#d56d2c)"></div><span>Diet &amp; Nutrition Personalisation</span></div>
      <div class="tile"><div class="thumb" role="img" aria-label="Children being picked up by a vehicle" style="background:linear-gradient(135deg,#9fc6e4,#4d7ea6)"></div><span>Pick Up Services</span></div>
      <div class="tile"><div class="thumb" role="img" aria-label="Pupils in a school classroom" style="background:linear-gradient(135deg,#d7c6a8,#8f7a5c)"></div><span>School Visits</span></div>
      <div class="tile"><div class="thumb" role="img" aria-label="Smiling child swimming in a pool" style="background:linear-gradient(135deg,#7fd0ec,#2b8fc4)"></div><span>Motivational Classes</span></div>
      <div class="tile"><div class="thumb" role="img" aria-label="Video preview of a class with play button" style="background:linear-gradient(135deg,#c7cacd,#7c8186)"></div><span>Know more..</span></div>
    </div>
  </section>

  <footer class="footer">
    <div class="links"><span>Home</span><i>|</i><span>About us</span><i>|</i><span>Services</span><i>|</i><span>Classes</span><i>|</i><span>News</span><i>|</i><span>Testimonials</span><i>|</i><span>Contact us</span></div>
    <div class="copy">Copyright © 2014 · Tumblewick Youth Sports Academy · All rights reserved</div>
    <div class="social"><span></span><span></span><span class="g"></span><span class="o"></span></div>
    <div class="badge"></div>
  </footer>
</div>
</body>
</html>
```